Sell Velvet Crumb Cheesecake Flyer

I am looking for a designer to help create an attractive sell sheet for my startup company, "Velvet Crumb". We want to build a brand in the cheesecake industry. Velvet Crumb takes a particular approach to preparing one of America’s favorite desserts. Cheesecake is beautiful in nature, so we put a greater emphasis on substance.

Target Market(s)

Lindmoor and Oakhaven County

Industry/Entity Type

It Company

Font styles to use
Sans Serif

Requirements
Must have
• I need the sheet created to include the following:
• Brand Logo, contact info, cheesecake images (not all), types of flavors, build your own options, sizes, prices, delivery availability(local only) and objective statement.I have a web address: www.tryvelvetcrumb.example, but its not active. email address: marna@tryvelvetcrumb.example
Nice to have
• As many images as possible but at least 4 or 5 of my top sellers. Apple, banana, cherry, strawberry shortcake and chocolate.

```html
<!DOCTYPE html>
<html lang="en">
<head>
<meta charset="utf-8">
<title>Velvet Crumb Sell Sheet</title>
<link href="https://fonts.googleapis.com/css2?family=Comfortaa:wght@400;700&family=Quicksand:wght@400;500&display=swap" rel="stylesheet">
<style>
  :root {
    --peach: #fde4d2;
    --peach-light: #fff6ef;
    --crimson: #c0263f;
    --magenta: #c81250;
    --gold: #f1b210;
    --oval: #fdd595;
    --brown: #5b3a28;
    --cake-cream: #efe2c4;
    --cake-choc: #6a4430;
  }
  html, body { margin: 0; padding: 0; overflow: hidden; }
  .sheet {
    position: relative;
    width: 1200px;
    height: 960px;
    overflow: hidden;
    background: radial-gradient(ellipse 70% 60% at 55% 55%, var(--peach-light) 0%, var(--peach) 75%);
    font-family: "Comfortaa", sans-serif;
    color: var(--crimson);
  }
  .band, .swoosh { position: absolute; left: 0; top: 0; }
  .brand {
    position: absolute;
    left: 52px; top: 120px;
    width: 200px;
    display: flex; flex-direction: column; align-items: center; gap: 10px;
  }
  .brand-mark { width: 44px; height: 44px; border-radius: 50%; background: var(--crimson); }
  .brand-name {
    font-size: 34px; font-weight: 700; line-height: 1.05; text-align: center;
    color: var(--crimson);
  }
  .about {
    position: absolute;
    left: 295px; top: 54px; width: 843px;
    font-size: 12px; line-height: 18.5px; letter-spacing: 0.4px;
    margin: 0; text-align: justify;
  }
  .tagline {
    position: absolute;
    left: 295px; top: 158px;
    font-size: 18.5px; font-weight: 700; margin: 0; letter-spacing: 0.3px;
  }
  .flavours {
    position: absolute;
    left: 542px; top: 192px; width: 304px; height: 466px;
    border-radius: 50%;
    background: radial-gradient(ellipse at center, var(--oval) 55%, rgba(253,213,149,0) 72%);
  }
  .flavour-list {
    list-style: none; margin: 0; padding: 30px 0 0;
    font-family: "Quicksand", sans-serif; font-weight: 500;
    font-size: 14.5px; line-height: 20px; text-align: center;
  }
  .options {
    position: absolute;
    left: 40px; top: 312px; width: 480px;
    font-family: "Quicksand", sans-serif; font-weight: 400;
    font-size: 24px; line-height: 30.5px; letter-spacing: 0.6px;
    text-align: center; margin: 0;
  }
  .cake {
    position: absolute;
    border-radius: 46% / 40%;
    box-shadow: 0 6px 10px rgba(0,0,0,0.25);
  }
  .cake-choc-drizzle { left: 0; top: 540px; width: 258px; height: 190px;
    background: linear-gradient(180deg, #b07a52 0%, var(--cake-choc) 45%, #1e1714 100%); }
  .cake-cookies { left: 258px; top: 584px; width: 274px; height: 180px;
    background: linear-gradient(180deg, #e6dcc0 0%, #d8ccaa 55%, #1e1714 100%); }
  .cake-strawberry { left: 458px; top: 704px; width: 292px; height: 184px;
    background: linear-gradient(180deg, #fbfaf6 0%, #d32a32 30%, var(--cake-cream) 60%, #1e1714 100%); }
  .cake-toffee { left: 772px; top: 740px; width: 306px; height: 214px;
    background: linear-gradient(180deg, #8a5a3a 0%, #b07548 50%, #1e1714 100%); }
  .cake-caramel { left: 924px; top: 556px; width: 276px; height: 180px;
    background: linear-gradient(180deg, #c88a3c 0%, var(--cake-cream) 40%, #e9dcc0 70%, #1e1714 100%); }
  .contact {
    position: absolute;
    left: 4px; top: 808px; width: 436px; height: 96px;
    border-radius: 50%;
    background: radial-gradient(ellipse at center, var(--oval) 50%, rgba(253,213,149,0) 72%);
  }
  .contact-lines {
    position: absolute; left: 54px; top: 824px; margin: 0;
    font-family: "Quicksand", sans-serif; font-weight: 500;
    font-size: 22px; line-height: 31px; letter-spacing: 1.4px;
    color: var(--brown);
  }
  .contact-lines a { color: inherit; text-decoration: none; display: block; }
</style>
</head>
<body>
<main class="sheet">
  <svg class="band" width="1200" height="960" viewBox="0 0 1200 960" aria-hidden="true">
    <path fill="var(--magenta)" d="M0,688 C200,672 420,740 640,768 C860,796 1040,730 1120,560 C1160,470 1185,360 1200,256 L1200,420 C1180,560 1130,690 1040,760 C940,836 780,848 640,830 C420,800 200,700 0,712 Z"/>
  </svg>
  <svg class="swoosh" width="1200" height="960" viewBox="0 0 1200 960" aria-hidden="true">
    <path fill="var(--gold)" d="M34,306 C70,400 120,460 210,462 C270,464 300,410 350,412 C380,414 410,440 430,478 C400,440 370,432 340,436 C300,444 270,470 210,470 C120,470 60,400 34,306 Z"/>
  </svg>

  <header class="brand">
    <span class="brand-mark"></span>
    <span class="brand-name">Velvet<br>Crumb</span>
  </header>

  <p class="about">Velvet Crumb, LLC is a local cheesecake company based out of Larkston, Ohio.&nbsp; At Velvet Crumb we strive to provide our customers with a food product that satisfies their greatest indulgence.<br>Velvet Crumb takes a particular approach to preparing one of America’s favorite desserts.&nbsp; Cheesecake is beautiful in nature, so we put a greater emphasis on substance. We don’t use a lot of bells and whistles, but we do add enough bold flavors to pleasure everyone’s palate.</p>
  <p class="tagline">Velvet Crumb is simple, made with a complex human need “Love”.</p>

  <p class="options">build your own options, sizes, prices,<br>delivery availability(local only)<br>and objective statement</p>

  <section class="flavours">
    <ul class="flavour-list">
      <li>Apple</li><li>Banana</li><li>Banana Split (baked or not)</li><li>Brownie Banana Split</li>
      <li>Carmel Toffee Brownie</li><li>Cherry</li><li>Chocolate</li><li>Chocolate Chip Cookie Dough</li>
      <li>Cookies &amp; Cream</li><li>Citrus</li><li>Maple Bacon</li><li>Peanut Butter</li>
      <li>Peanut Butter Brownie</li><li>Peanut Butter Pretzel</li><li>Lemon Blueberry</li>
      <li>Strawberry Shortcake</li><li>Smores</li><li>Sweet Potato</li><li>White Chocolate Raspberry</li>
    </ul>
  </section>

  <div class="cake cake-choc-drizzle" role="img" aria-label="Photo of a chocolate cheesecake with white drizzle on a cake board"></div>
  <div class="cake cake-cookies" role="img" aria-label="Photo of a cookies and cream cheesecake on a cake board"></div>
  <div class="cake cake-caramel" role="img" aria-label="Photo of a caramel crumble cheesecake on a cake board"></div>
  <div class="cake cake-strawberry" role="img" aria-label="Photo of a strawberry shortcake cheesecake topped with cream"></div>
  <div class="cake cake-toffee" role="img" aria-label="Photo of a toffee brownie cheesecake on a cake board"></div>

  <div class="contact" aria-hidden="true"></div>
  <address class="contact-lines">
    <a href="#">www.tryvelvetcrumb.example</a>
    <a href="#">marna@tryvelvetcrumb.example</a>
  </address>
</main>
</body>
</html>
```